【サイトマップ】
1 TOP
2 Lumora Styleとは
3 お客様の声(一覧)
4 お客様の声(詳細)
5 ブログ(一覧)
6 ブログ(詳細)
7 お知らせ(一覧)
8 お知らせ(詳細)
9 イベント情報(一覧)
10 イベント情報(詳細)
11 お問い合わせ
12 Q&A
13 商品ページ(一覧)
14 商品ページ(詳細)
15 ライター紹介ページ

【要望】
情報発信サイトのため静的なページは最低限押さえ動的なコンテンツを盛り込んでおります。
各ページの意図を説明しておきます。

<ブログ>
いわゆるコラムページです。季節に合わせた着こなしやおすすめのコーディネートなどを紹介していきます。

<お客様の声>
商品レビュー。ECで購入した商品についてお客様の感想を掲載します。

<イベント情報>
着こなし講座。お食事会などイベントについて掲載していきます。

<商品ページ>
ライターが連動しているECサイトから商品をピックアップし記事として取り上げます。

<ライター紹介ページ>
まずはライターは2名体勢で指導しますが今後増やしていく予定です。
TOPに2名分の枠を用意頂ければと思います。
参考:https://norbeta.co.jp/member

■HPのメインターゲット
30、40代の方(女性のみ)

■サイトのデザインにおける優先事項
見やすさ > デザイン性(写真・画像量)

■HPに望む効果
・新規顧客獲得
ECサイトも立ち上げ前なので、とにかくサイトのファンを付けたいと考えております。
そのため「人目につくサイト」「定期的にチェックしてみたいと思ってもらえるサイト」を目指しております。
ページ数
1ページ
希望イメージ
シンプル 複雑
単色 カラフル
暗い 明るい
日常 高級
遊び心 厳粛
未来的 伝統的
女性的 男性的
希望する色
特にございません。いろんな提案を見てみたいのが正直なところです。
納品ファイル
• イラストレーター形式 (.ai)
• フォトショップ形式 (.psd)
• PNG形式 (.png)
補足説明
<店舗へのご連絡はおやめください>
ジョブリオの規約にもありますが、店舗様の通常業務に支障が出るため・素材について直接電話等のお問い合わせをお控えいただきますよう、ご協力の程お願いいたします。

-----------------------------------------------------------------------

<素材はPixmoraかその他無償の素材をご使用ください>
素材として必要なものがある場合にはピクモラ画像をご使用ください。
疑問や不明点などがありましたら、ジョブリオ内メッセージにて頂戴できますと幸いです。

その際、定期契約でダウンロード出来る画像のみを使用してください。
(画像検索した際に出てくるサムネール下の画像番号の横に
ピクモラのマークがあるものは使用しないようお願いいたします。)

ピクモラ以外の素材を使用する際には、
必ず無料で提供いただける物のみご使用ください。
もう少し提案を見たいため延長させて頂きます。
もう少し提案が見たいため、延長させて頂きます。
本日より1週間募集期間を延長致します。
引き続き宜しくお願い致します。
沢山のご提案をありがとうございます。
最後にあと一週間だけ期間を延長させていただきます。
引き続き、何卒宜しくお願い致します。

ひと目見て気に入りました。

みなさまご提案ありがとうございました。

```html
<!DOCTYPE html>
<html lang="ja">
<head>
<meta charset="utf-8">
<title>Lumora Style</title>
<link href="https://fonts.googleapis.com/css2?family=Noto+Sans+JP:wght@400;500;700&family=Josefin+Sans:wght@400;600&display=swap" rel="stylesheet">
<style>
:root{
  --ink:#333333;
  --sub:#888888;
  --line:#dddddd;
  --bg:#f1f1f1;
  --white:#ffffff;
  --accent:#e5506f;
  --teal:#3fa7b5;
  --dark:#2f2f2f;
}
*{box-sizing:border-box;margin:0;padding:0}
html,body{width:1200px;height:3848px;overflow:hidden}
body{font-family:"Noto Sans JP",sans-serif;color:var(--ink);background:var(--bg);font-size:13px;line-height:1.6;position:relative}
a{color:inherit;text-decoration:none}
.photo{display:block}

/* header */
.site-header{position:absolute;top:0;left:0;width:1200px;height:108px;background:var(--white)}
.brand-name{position:absolute;left:24px;top:30px;font-size:30px;font-weight:500;letter-spacing:.04em;line-height:1.2}
.util{position:absolute;right:24px;top:12px;display:flex;gap:22px;font-size:11px;color:var(--sub)}
.util span{display:flex;align-items:center;gap:6px}
.util i{width:14px;height:14px;border-radius:50%;background:var(--ink);display:inline-block}
.search{position:absolute;right:24px;top:46px;width:260px;height:32px;border:1px solid var(--line);font-size:11px;color:#aaa;padding:6px 10px;display:flex;justify-content:space-between;align-items:center}
.global-nav{position:absolute;top:108px;left:0;width:1200px;height:44px;background:var(--white);border-top:1px solid var(--line);border-bottom:1px solid var(--line);display:flex;justify-content:space-between;align-items:center;padding:0 28px 0 24px;font-size:13px;font-weight:500}
.global-nav a+a{border-left:1px solid var(--line);padding-left:36px}

/* hero */
.hero{position:absolute;top:152px;left:0;width:1200px;height:520px;background:var(--white);overflow:hidden}
.slide{position:absolute;top:8px;width:500px}
.slide .photo{width:496px;height:320px}
.slide .cap{padding:12px 14px 0}
.meta{font-size:11px;color:var(--sub);display:flex;gap:10px;align-items:center}
.new{color:var(--accent);font-weight:700}
.slide h3{font-size:16px;font-weight:700;line-height:1.5;margin-top:4px}
.arrow-r{position:absolute;right:8px;top:150px;font-size:32px;color:var(--white)}
.dots{position:absolute;top:624px;left:0;width:1200px;display:flex;justify-content:center;gap:12px}
.dots i{width:8px;height:8px;border-radius:50%;background:#c8c8c8;display:block}
.dots i:first-child{background:#777}

/* layout */
.main{position:absolute;top:672px;left:100px;width:680px}
.side{position:absolute;top:672px;left:820px;width:280px}
.card{background:var(--white);padding:28px 32px}
.sec-title{display:flex;align-items:baseline;gap:12px;margin-bottom:22px}
.sec-title h2{font-family:"Josefin Sans",sans-serif;font-size:26px;font-weight:600;letter-spacing:.04em}
.sec-title small{font-size:11px;color:var(--sub)}
.more{display:flex;justify-content:space-between;align-items:center;width:340px;height:36px;margin:26px auto 40px;background:var(--white);border:1px solid var(--line);padding:0 16px;font-size:12px}
.more::before{content:"";width:10px}

/* pick up */
.pick-grid{display:grid;grid-template-columns:1fr 1fr;gap:22px 28px}
.pick-grid .photo{width:294px;height:190px}
.pick-grid p{font-size:12px;margin-top:8px}

/* new entry */
.entry{display:flex;gap:22px;padding:18px 0;border-top:1px solid #eeeeee}
.entry:first-of-type{border-top:none;padding-top:0}
.entry .photo{width:170px;height:124px;flex:none}
.entry h3{font-size:15px;font-weight:700;line-height:1.5}
.entry .meta{margin:4px 0 6px}
.entry p{font-size:12px;color:#666;line-height:1.7}
.read{font-size:11px;font-weight:700;margin-top:6px}

/* events */
.events{display:grid;grid-template-columns:1fr 1fr;gap:28px}
.events .photo{width:294px;height:160px}
.ev-meta{display:flex;justify-content:space-between;align-items:center;margin:10px 0 6px;font-size:11px;color:var(--sub)}
.tag{color:var(--white);font-size:10px;padding:2px 8px}
.tag.open{background:var(--teal)}
.tag.closed{background:var(--accent)}
.events h3{font-size:14px;font-weight:700;color:var(--accent);line-height:1.5}
.events p{font-size:11px;color:#666;margin-top:6px}

/* writer */
.writers{display:flex;gap:40px;padding-left:10px}
.writer{text-align:center;width:170px}
.writer .photo{width:170px;height:170px;border-radius:50%}
.writer p{margin-top:12px;font-size:12px}

/* share */
.share{position:relative;border:1px solid #cfcfcf;height:120px;margin-top:20px;display:flex;justify-content:center;align-items:center;gap:58px}
.share h4{position:absolute;top:-10px;left:24px;background:var(--bg);padding:0 10px;font-family:"Josefin Sans",sans-serif;font-size:14px;letter-spacing:.1em}
.share i{width:28px;height:28px;background:var(--ink);border-radius:4px;display:block}

/* sidebar */
.store-link{background:var(--white);border:1px solid var(--line);height:128px;display:flex;flex-direction:column;align-items:center;justify-content:center;gap:10px}
.store-name{display:flex;align-items:center;gap:10px;font-size:22px;font-weight:500;letter-spacing:.03em;line-height:1.2}
.store-name i{width:12px;height:12px;background:var(--ink);display:block}
.store-link span{font-size:12px;color:var(--sub)}
.widget{background:var(--white);margin-top:22px;padding:18px 20px}
.widget h3{display:flex;align-items:center;gap:10px;font-size:13px;font-weight:700;border-bottom:1px solid var(--line);padding-bottom:12px;margin-bottom:10px}
.widget h3 i{width:14px;height:14px;background:var(--ink);display:block;border-radius:50%}
.widget h3 em{margin-left:auto;font-style:normal;color:var(--sub)}
.widget li{list-style:none;font-size:11px;padding:7px 0;border-bottom:1px dotted var(--line)}
.widget li small{display:block;color:var(--sub);font-size:10px}
.widget li.hot{color:var(--accent)}
.voice-date{display:block;font-size:10px;color:var(--sub)}
.voice-title{font-size:11px}
.voice .photo{width:240px;height:150px;margin:8px 0 4px}
.side-banner{margin-top:22px;width:280px;height:160px}

/* footer */
.site-footer{position:absolute;top:3492px;left:0;width:1200px;height:248px;background:var(--dark);color:#ddd;padding:40px 100px}
.f-name{font-size:26px;font-weight:500;letter-spacing:.03em;color:var(--white);line-height:1.3}
.f-tag{font-size:10px;color:#aaa;margin-top:6px;line-height:1.6}
.f-sns{display:flex;gap:12px;margin-top:16px}
.f-sns i{width:18px;height:18px;border-radius:50%;background:#ddd;display:block}
.f-cols{position:absolute;left:380px;top:46px;display:flex;gap:56px;font-size:11px}
.f-cols h4{font-size:11px;font-weight:700;color:var(--white);margin-bottom:10px}
.f-cols li{list-style:none;line-height:1.9;color:#bbb}
.f-store{position:absolute;right:100px;top:60px;width:160px;height:140px;border:1px solid #777;color:var(--white);display:flex;flex-direction:column;align-items:center;justify-content:center;gap:8px}
.f-store b{font-size:17px;font-weight:500;line-height:1.2}
.f-store span{font-size:11px;color:#bbb}
.bottom-bar{position:absolute;top:3740px;left:0;width:1200px;height:108px;background:var(--white);display:flex;justify-content:space-between;align-items:center;padding:0 100px;font-size:11px;color:var(--sub)}
.bottom-bar nav{display:flex;gap:28px}
</style>
</head>
<body>

<header class="site-header">
  <div class="brand-name">Lumora Style</div>
  <div class="util"><span><i></i>初めての方へ</span><span><i></i>お問合せ</span><span><i></i>よくある質問</span><span><i></i>会員登録</span></div>
  <div class="search">気になるワードを検索 <svg width="12" height="12" viewBox="0 0 12 12"><circle cx="5" cy="5" r="4" fill="none" stroke="#999" stroke-width="1.5"/><line x1="8" y1="8" x2="11" y2="11" stroke="#999" stroke-width="1.5"/></svg></div>
</header>
<nav class="global-nav">
  <a>ファッションニュース</a><a>コーディネート講座</a><a>美容・健康</a><a>ライフスタイル</a><a>季節のお楽しみ</a><a>おすすめアイテム</a><a>イベント情報</a>
</nav>

<section class="hero">
  <div class="slide" style="left:-400px"><span class="photo" role="img" aria-label="Fashion photo of a woman outdoors" style="background:linear-gradient(#a79a8c,#6f665d)"></span><div class="cap"><div class="meta">2016.10.15 ファッションニュース <span class="new">NEW</span></div><h3>こちらに記事タイトルが入ります<br>こちらに記事タイ</h3></div></div>
  <div class="slide" style="left:100px"><span class="photo" role="img" aria-label="Woman in a white dress walking with a bicycle" style="background:linear-gradient(135deg,#8e9b8a,#5f6d5d)"></span><div class="cap"><div class="meta">2016.10.15 ファッションニュース <span class="new">NEW</span></div><h3>こちらに記事タイトルが入ります</h3></div></div>
  <div class="slide" style="left:600px"><span class="photo" role="img" aria-label="Woman standing in a sunlit forest" style="background:linear-gradient(135deg,#6e7658,#3f4634)"></span><div class="cap"><div class="meta">2016.10.15 ファッションニュース <span class="new">NEW</span></div><h3>こちらに記事タイトルが入りますこちらに記事タイ<br>トルが入ります</h3></div></div>
  <div class="slide" style="left:1100px"><span class="photo" role="img" aria-label="Woman in a light skirt on a field" style="background:linear-gradient(135deg,#c9c2b5,#9c9584)"></span><div class="cap"><div class="meta">2016.10.15</div><h3>こちらに記事</h3></div></div>
  <div class="arrow-r">›</div>
</section>
<div class="dots"><i></i><i></i><i></i><i></i><i></i><i></i></div>

<main class="main">
  <section class="card">
    <div class="sec-title"><h2>PICK UP ITEM</h2><small>— おすすめアイテム</small></div>
    <div class="pick-grid">
      <div><span class="photo" role="img" aria-label="Striped knit and accessories flat lay" style="background:linear-gradient(135deg,#cfd3da,#6b7383)"></span><p>こちらに商品ページタイトルが入ります</p></div>
      <div><span class="photo" role="img" aria-label="Leather bag and small items" style="background:linear-gradient(135deg,#b58d68,#6d4c33)"></span><p>こちらに商品ページタイトルが入ります</p></div>
      <div><span class="photo" role="img" aria-label="Woman in a blue coat" style="background:linear-gradient(135deg,#9fb6c9,#4f6c86)"></span><p>こちらに商品ページタイトルが入ります</p></div>
      <div><span class="photo" role="img" aria-label="Knit scarf and coffee on a table" style="background:linear-gradient(135deg,#d59a8e,#5f6f88)"></span><p>こちらに商品ページタイトルが入ります</p></div>
    </div>
  </section>
  <a class="more">おすすめアイテム一覧はこちら <span>›</span></a>

  <section class="card">
    <div class="sec-title"><h2>NEW ENTRY</h2><small>— 新着記事</small></div>
    <article class="entry"><span class="photo" role="img" aria-label="Woman with a bicycle" style="background:linear-gradient(135deg,#97a290,#5d6859)"></span><div><h3>こちらに記事タイトルが入ります<br>こちらに記事タイトルが入ります</h3><div class="meta">2016.10.15 ファッションニュース</div><p>こちらに記事の概要文が入ります。こちらに記事の概要文が入ります。<br>季節の着こなしについてご紹介します。</p><div class="read">つづきを読む ›</div></div></article>
    <article class="entry"><span class="photo" role="img" aria-label="Woman in a forest" style="background:linear-gradient(135deg,#6e7658,#3f4634)"></span><div><h3>こちらに記事タイトルが入りますこちらに記事<br>タイトルが入ります</h3><div class="meta">2016.10.14 コーディネート講座</div><p>こちらに記事の概要文が入ります。こちらに記事の概要文が入ります。<br>季節の着こなしについてご紹介します。</p><div class="read">つづきを読む ›</div></div></article>
    <article class="entry"><span class="photo" role="img" aria-label="Woman resting on a rug" style="background:linear-gradient(135deg,#5b4f47,#2e2824)"></span><div><h3>こちらに記事タイトルが入りますこちらに記事<br>タイトルが入ります</h3><div class="meta">2016.10.13 美容・健康</div><p>こちらに記事の概要文が入ります。こちらに記事の概要文が入ります。<br>季節の着こなしについてご紹介します。</p><div class="read">つづきを読む ›</div></div></article>
    <article class="entry"><span class="photo" role="img" aria-label="Woman on a field in autumn" style="background:linear-gradient(135deg,#c7b7a2,#7a6a56)"></span><div><h3>こちらに記事タイトルが入ります</h3><div class="meta">2016.10.12 ライフスタイル</div><p>こちらに記事の概要文が入ります。こちらに記事の概要文が入ります。<br>季節の着こなしについてご紹介します。</p><div class="read">つづきを読む ›</div></div></article>
  </section>
  <a class="more">ブログ記事一覧はこちら <span>›</span></a>

  <section class="card">
    <div class="sec-title"><h2>SHOP EVENT</h2><small>— イベント情報</small></div>
    <div class="events">
      <div><span class="photo" role="img" aria-label="Autumn coordinate lesson event visual" style="background:linear-gradient(135deg,#8a6a4f,#3e2e22)"></span><div class="ev-meta"><span class="tag open">募集中</span>2016.10.15</div><h3>こちらにイベントタイトルが入りますこちらにイベントタイトルが入ります</h3><p>日時：2016.10.20(木) 10:00〜18:00<br>場所：イベント会場名が入ります</p></div>
      <div><span class="photo" role="img" aria-label="Tea party event visual" style="background:linear-gradient(135deg,#a36f6d,#4e3433)"></span><div class="ev-meta"><span class="tag closed">受付終了</span>2016.10.10</div><h3>こちらにイベントタイトルが入りますこちらにイベントタイトルが入ります</h3><p>日時：2016.10.12(水) 10:00〜18:00<br>場所：イベント会場名が入ります</p></div>
    </div>
  </section>
  <a class="more">イベント情報一覧はこちら <span>›</span></a>

  <section class="card">
    <div class="sec-title"><h2>WRITER</h2><small>— ライター紹介</small></div>
    <div class="writers">
      <div class="writer"><span class="photo" role="img" aria-label="Writer portrait" style="background:radial-gradient(circle,#d8c4a6,#8b6e4e)"></span><p>ライター名</p></div>
      <div class="writer"><span class="photo" role="img" aria-label="Writer portrait" style="background:radial-gradient(circle,#e1e1e1,#8c8c8c)"></span><p>ライター名</p></div>
    </div>
  </section>
  <a class="more">くわしいプロフィールはこちら <span>›</span></a>

  <div class="share"><h4>SHARE</h4><i></i><i></i><i></i><i></i><i></i><i></i><i></i><i></i></div>
</main>

<aside class="side">
  <a class="store-link"><div class="store-name"><i></i>Lumora Style</div><span>オンラインストアはこちら ›</span></a>
  <div class="widget">
    <h3><i></i>お知らせ<em>›</em></h3>
    <ul>
      <li><small>2016.10.15</small>こちらにお知らせタイトルが入ります</li>
      <li><small>2016.10.12</small>こちらにお知らせタイトルが入ります</li>
      <li><small>2016.10.08</small>こちらにお知らせタイトルが入ります</li>
      <li><small>2016.10.01</small>こちらにお知らせタイトルが入ります</li>
    </ul>
  </div>
  <div class="widget">
    <h3><i></i>よくある質問<em>›</em></h3>
    <ul>
      <li class="hot">こちらによくある質問が入ります</li>
      <li class="hot">こちらによくある質問が入ります</li>
      <li>こちらによくある質問が入ります</li>
      <li>こちらによくある質問が入ります</li>
    </ul>
  </div>
  <div class="widget voice">
    <h3><i></i>お客様の声<em>›</em></h3>
    <small class="voice-date">2016.10.15</small>
    <p class="voice-title">こちらにお客様の声のタイトルが入ります</p>
    <span class="photo" role="img" aria-label="Customer wearing a pink outfit" style="background:linear-gradient(135deg,#f1c7cc,#c7838d)"></span>
    <small class="voice-date">2016.10.10</small>
    <p class="voice-title">こちらにお客様の声のタイトルが入ります</p>
    <span class="photo" role="img" aria-label="Customer in autumn clothes" style="background:linear-gradient(135deg,#8a7f72,#4a443d)"></span>
  </div>
  <div class="widget">
    <h3><i></i>月別アーカイブ<em>›</em></h3>
    <ul>
      <li>2016年10月</li>
      <li>2016年9月</li>
      <li>2016年8月</li>
    </ul>
  </div>
  <span class="photo side-banner" role="img" aria-label="Campaign banner with a woman" style="background:linear-gradient(135deg,#6c8a90,#2f4447)"></span>
  <span class="photo side-banner" role="img" aria-label="Feature banner with a woman" style="background:linear-gradient(135deg,#b7a38c,#6e5d4a)"></span>
</aside>

<footer class="site-footer">
  <div class="f-name">Lumora Style</div>
  <p class="f-tag">30代・40代の女性のための<br>ファッション情報サイト</p>
  <div class="f-sns"><i></i><i></i><i></i><i></i><i></i></div>
  <div class="f-cols">
    <div><h4>カテゴリー一覧</h4><ul><li>ファッションニュース</li><li>コーディネート講座</li><li>美容・健康</li><li>ライフスタイル</li></ul></div>
    <div><h4>SHOP</h4><ul><li>おすすめアイテム</li><li>イベント情報</li><li>お客様の声</li><li>ライター紹介</li></ul></div>
    <div><h4>サイトについて</h4><ul><li>初めての方へ</li><li>お知らせ</li><li>よくある質問</li><li>お問い合わせ</li></ul></div>
  </div>
  <a class="f-store"><b>Lumora Style</b><span>オンラインストア ›</span></a>
</footer>
<div class="bottom-bar">
  <span>© 2016 Lumora Style All Rights Reserved.</span>
  <nav><a>運営会社</a><a>利用規約</a><a>ライター募集</a></nav>
</div>

</body>
</html>
```